Owen Pellick Personal Website Yoga Teacher and Personal Fitness Trainer

Let's pick a WORDPRESS theme that can work with Video Bckground. I would like a website design to look like some of nice Squarespace themes.
I would like to have a Video background of me teaching. I can provide video. Please view my current Wordpress site: www.owenpellick.com. I also have new logo. See file opelk1.png
Updates

Project Deadline Extended
Reason: I am guaranteeing this project because i believe designers can deliver. I am extending 5 days because the homepage image/video slider is intricate and takes a bit of time. I have provided details, images, video etc. in Dropbox. Tx

Target Market(s)

All people needing & wanting personal help (they can trust and feel safe and nurtured) for their health (wellness, nutrition, fitness, exercise). And people wanting extraordinary yoga teaching.

Industry/Entity Type

Fitness

Number of Pages Required

5+ page

Colors
9bcb3b
add136
cadf82
eaf2ce

Requirements
Must have
• Template that can use a video background
Nice to have
• Need to show good image gallery and testimonial videos

```html
<!DOCTYPE html>
<html lang="en">
<head>
<meta charset="utf-8">
<title>Owen Pellick — Yoga &amp; Wellness</title>
<link href="https://fonts.googleapis.com/css2?family=Lato:wght@300;400;700&family=Open+Sans:wght@600;700&family=Roboto:wght@300;400&display=swap" rel="stylesheet">
<style>
:root{
  --green:#6e9a4b;
  --green-text:#5f9a2e;
  --leaf:#7dae3e;
  --teal-line:#4fb58a;
  --ink:#222;
  --grey:#5a5a5a;
  --muted:#999;
  --red:#e05a5a;
  --navy:#1f2d3d;
}
*{box-sizing:border-box;margin:0;padding:0}
html,body{width:960px;height:1200px;overflow:hidden;background:#fff}
.page{position:relative;width:1200px;height:1500px;transform:scale(.8);transform-origin:0 0;font-family:'Lato',sans-serif;color:var(--grey)}
.abs{position:absolute}
.photo{position:absolute}

/* hero */
.hero{left:240px;top:0;width:720px;height:363px;background:linear-gradient(90deg,#e8a03c 0%,#f4d9a8 12%,#f6ecd9 35%,#eadbc1 60%,#c9a57b 85%,#8a6a4a 100%)}
.hero-floor{left:240px;top:300px;width:720px;height:63px;background:linear-gradient(180deg,rgba(120,90,60,.1),rgba(90,70,50,.6))}
.logo{left:248px;top:26px;display:flex;align-items:center;gap:7px;white-space:nowrap}
.logo-mark{width:28px;height:28px;border-radius:50%;border:2px solid var(--leaf);flex:none}
.logo-name{font-size:17px;font-weight:700;color:var(--green-text);letter-spacing:0}
.nav{left:436px;top:28px;width:524px;height:24px;background:rgba(255,255,255,.55);display:flex;justify-content:flex-end;align-items:center;gap:10px;padding-right:6px}
.nav a{font-size:13.5px;color:var(--green-text);text-decoration:none}
.caption{left:305px;top:150px;width:300px;height:132px;background:rgba(255,255,255,.45);padding:6px 10px}
.caption h2{font-size:19px;font-weight:700;color:var(--green-text);white-space:nowrap}
.caption p{width:262px;font-size:11.5px;line-height:14.5px;color:#6a6a6a;margin-top:4px}
.caption a{color:var(--green-text);text-decoration:none}
.round-arrow{width:18px;height:18px;border-radius:50%;background:rgba(255,255,255,.6);display:flex;align-items:center;justify-content:center}
.dots{left:583px;top:341px;display:flex;gap:6px}
.dots i{width:8px;height:8px;border-radius:50%;border:1px solid #fff}
.dots i.on{background:#fff}

/* about */
.about-title{left:240px;top:382px;width:720px;text-align:center;font-family:'Open Sans',sans-serif;font-weight:700;font-size:21px;color:var(--green-text)}
.about-text{left:255px;top:416px;width:700px;text-align:center;font-family:'Open Sans',sans-serif;font-weight:600;font-size:12.3px;line-height:14.8px;color:#555}

/* story */
.story-icon{left:243px;top:510px;width:30px;height:30px;background:var(--red);display:flex;align-items:center;justify-content:center}
.story-title{left:289px;top:512px;font-family:'Roboto',sans-serif;font-size:18px;line-height:22px;color:#333}
.story-time{left:289px;top:565px;font-family:'Roboto',sans-serif;font-weight:300;font-size:10px;color:var(--muted)}
.story-text{left:289px;top:604px;width:172px;font-family:'Roboto',sans-serif;font-weight:300;font-size:11px;line-height:18px;color:#555}
.story-text a{color:var(--green-text);text-decoration:none}
.actions{left:478px;top:483px;width:78px;height:225px;background:var(--green);display:flex;flex-direction:column;align-items:center;padding-top:20px;gap:26px}
.action{display:flex;flex-direction:column;align-items:center;gap:5px;color:#fff;font-family:'Roboto',sans-serif;font-size:12px}
.video{left:556px;top:483px;width:404px;height:225px;background:linear-gradient(90deg,#f3e6cf 0%,#f0dcc0 40%,#d9a37a 65%,#c98c5c 80%,#e8d2b2 100%)}
.play{left:724px;top:569px;width:48px;height:48px;border-radius:50%;background:var(--navy);display:flex;align-items:center;justify-content:center}
.next-btn{left:929px;top:580px;width:23px;height:23px;border-radius:50%;background:#fff;display:flex;align-items:center;justify-content:center}

/* classes & events */
.section-h{font-size:18px;color:var(--green-text);font-weight:400}
.classes{left:246px;top:777px;width:345px;height:192px;background:var(--green);padding:0 22px 0 18px}
.class-row{height:48px;display:flex;align-items:center;border-bottom:1px solid rgba(255,255,255,.45)}
.class-row:last-child{border-bottom:none}
.class-row .name{flex:1;margin-left:9px;color:#fff;font-size:13.5px;font-weight:700}
.class-row .tools{display:flex;gap:19px;margin-right:12px}
.events{left:609px;top:777px;width:351px;height:192px;border:1.5px solid var(--teal-line)}
.event{position:absolute;left:9px;width:330px;height:74px}
.event .thumb{position:absolute;left:0;top:0;width:112px;height:74px}
.event .body{position:absolute;left:127px;top:-2px}
.event .date{font-size:14px;color:#111}
.event .name{font-size:14px;color:var(--green-text);margin-top:2px}
.event p{font-size:10.5px;line-height:18px;color:#555;margin-top:1px}

/* blog */
.pager{display:flex;gap:3px}
.post-date{font-size:14px;line-height:18px;color:#111}
.post-rule{width:1px;height:160px;background:#c9d9b8}
.post-icons{display:flex;flex-direction:column;gap:13px}
.post-img{width:120px;height:78px}
.post-by{font-size:10.5px;color:#555}
.post-by span{color:var(--green-text)}
.post-title{font-size:14px;color:var(--green-text)}
.post-text{width:290px;font-size:10.5px;line-height:18px;color:#444}

/* gallery & footer */
.gallery-item{top:1272px;width:134px;height:133px}
.copyright{left:240px;top:1437px;width:720px;text-align:center;font-size:12px;color:#666}
.social{top:1427px;width:25px;height:25px;border-radius:50%}
</style>
</head>
<body>
<div class="page">

  <!-- hero -->
  <div class="photo hero" role="img" aria-label="Man meditating cross-legged on a yoga mat in a sunlit room with sheer curtains"></div>
  <div class="abs hero-floor"></div>
  <div class="abs logo"><span class="logo-mark"></span><span class="logo-name">OWEN PELLICK</span></div>
  <nav class="abs nav">
    <a href="#">Home</a><a href="#">About</a><a href="#">Blog</a><a href="#">Clients</a><a href="#">Contact</a><a href="#">Media</a><a href="#">Nutrition</a><a href="#">Schedule/Classes</a><a href="#">Services</a>
  </nav>
  <div class="abs caption">
    <h2>Be the Healthiest &amp; Happiest YOU!</h2>
    <p>I practice a holistic approach to nutrition, which means that I look at how all areas of your life are connected. Does stress at your job or in your rela-tionship cause you to overeat? Does lack of sleep or low energy prevent you from exercising? As we work together, we look at.. <a href="#">read more</a></p>
  </div>
  <div class="abs round-arrow" style="left:245px;top:191px"><svg width="10" height="10" viewBox="0 0 10 10"><path d="M8 5H2M5 2L2 5l3 3" stroke="#888" stroke-width="1.5" fill="none"/></svg></div>
  <div class="abs round-arrow" style="left:934px;top:191px"><svg width="10" height="10" viewBox="0 0 10 10"><path d="M2 5h6M5 2l3 3-3 3" stroke="#888" stroke-width="1.5" fill="none"/></svg></div>
  <div class="abs dots"><i></i><i class="on"></i><i></i><i></i></div>

  <!-- about -->
  <h1 class="abs about-title">Who Am I</h1>
  <p class="abs about-text">Lorem ipsum dolor sit amet, consectetur adipiscing elit. Curabitur at nulla mauris. Mauris consequat lectus gravida feugiat aliquet. Integer tempor volutpat mi eget pellentesque. Pellentesque maximus faucibus metus vitae mollis. Fusce rutrum eleifend diam. Nullam in risus eros. Nam lacinia metus velit, sit amet ultricies dui fringilla vitae.</p>

  <!-- story -->
  <div class="abs story-icon"><svg width="16" height="12" viewBox="0 0 16 12"><rect x="0" y="2" width="10" height="8" rx="1" fill="#fff"/><path d="M10 6l6-4v8z" fill="#fff"/></svg></div>
  <h3 class="abs story-title" style="font-weight:400">Best story you<br>have ever heard</h3>
  <div class="abs story-time">24 minutes ago</div>
  <p class="abs story-text">Lorem Ipsum is simply dummy text of the printing and typesetting industry. Lorem ipsum has been the industry's... <a href="#">Read more</a></p>
  <div class="abs actions">
    <div class="action"><svg width="26" height="24" viewBox="0 0 26 24"><path d="M13 22S2 15 2 8a5.5 5.5 0 0 1 11-1 5.5 5.5 0 0 1 11 1c0 7-11 14-11 14z" fill="none" stroke="#fff" stroke-width="2"/></svg>Like</div>
    <div class="action"><svg width="26" height="26" viewBox="0 0 26 26"><circle cx="13" cy="13" r="11" fill="none" stroke="#fff" stroke-width="2"/><path d="M13 6v7h-5" fill="none" stroke="#fff" stroke-width="2"/></svg>Later</div>
    <div class="action"><svg width="26" height="24" viewBox="0 0 26 24"><path d="M4 9v13h18v-7" fill="none" stroke="#fff" stroke-width="2"/><path d="M9 15c1-6 6-8 11-8V3l5 5-5 5V10c-4 0-8 1-11 5z" fill="#fff"/></svg>Share</div>
  </div>
  <div class="photo video" role="img" aria-label="Video still of a man in an orange shirt doing a seated twist on a yoga mat"></div>
  <div class="abs play"><svg width="18" height="20" viewBox="0 0 18 20"><path d="M2 1l15 9-15 9z" fill="#fff"/></svg></div>
  <div class="abs next-btn"><svg width="10" height="10" viewBox="0 0 10 10"><path d="M3 1l4 4-4 4" stroke="#999" stroke-width="1.5" fill="none"/></svg></div>

  <!-- classes -->
  <h2 class="abs section-h" style="left:246px;top:740px;width:345px;text-align:center">ALL CLASSES</h2>
  <div class="abs classes">
    <div class="class-row"><svg width="18" height="18" viewBox="0 0 18 18"><circle cx="9" cy="9" r="7.5" fill="none" stroke="#fff" stroke-width="2"/><path d="M9 5v4H6" stroke="#fff" stroke-width="1.8" fill="none"/></svg><span class="name">Beginner Yoga</span><span class="tools"><svg width="15" height="15" viewBox="0 0 15 15"><rect x="1" y="2.5" width="13" height="11.5" fill="none" stroke="#fff" stroke-width="1.3"/><path d="M1 6h13M4 1v3M11 1v3M4 8.5h7M4 11h7M6 6v8M9 6v8" stroke="#fff" stroke-width="1"/></svg><svg width="16" height="14" viewBox="0 0 26 24"><path d="M13 22S2 15 2 8a5.5 5.5 0 0 1 11-1 5.5 5.5 0 0 1 11 1c0 7-11 14-11 14z" fill="none" stroke="#fff" stroke-width="2.6"/></svg><svg width="16" height="14" viewBox="0 0 16 14"><path d="M1 13c1-6 5-8 10-8V1l5 5-5 5V8c-4 0-8 1-10 5z" fill="#fff"/></svg></span></div>
    <div class="class-row"><svg width="18" height="18" viewBox="0 0 18 18"><circle cx="9" cy="9" r="7.5" fill="none" stroke="#fff" stroke-width="2"/><path d="M9 5v4H6" stroke="#fff" stroke-width="1.8" fill="none"/></svg><span class="name">Nutritions</span><span class="tools"><svg width="15" height="15" viewBox="0 0 15 15"><rect x="1" y="2.5" width="13" height="11.5" fill="none" stroke="#fff" stroke-width="1.3"/><path d="M1 6h13M4 1v3M11 1v3M4 8.5h7M4 11h7M6 6v8M9 6v8" stroke="#fff" stroke-width="1"/></svg><svg width="16" height="14" viewBox="0 0 26 24"><path d="M13 22S2 15 2 8a5.5 5.5 0 0 1 11-1 5.5 5.5 0 0 1 11 1c0 7-11 14-11 14z" fill="none" stroke="#fff" stroke-width="2.6"/></svg><svg width="16" height="14" viewBox="0 0 16 14"><path d="M1 13c1-6 5-8 10-8V1l5 5-5 5V8c-4 0-8 1-10 5z" fill="#fff"/></svg></span></div>
    <div class="class-row"><svg width="18" height="18" viewBox="0 0 18 18"><circle cx="9" cy="9" r="7.5" fill="none" stroke="#fff" stroke-width="2"/><path d="M9 5v4H6" stroke="#fff" stroke-width="1.8" fill="none"/></svg><span class="name">Advanced Yoga</span><span class="tools"><svg width="15" height="15" viewBox="0 0 15 15"><rect x="1" y="2.5" width="13" height="11.5" fill="none" stroke="#fff" stroke-width="1.3"/><path d="M1 6h13M4 1v3M11 1v3M4 8.5h7M4 11h7M6 6v8M9 6v8" stroke="#fff" stroke-width="1"/></svg><svg width="16" height="14" viewBox="0 0 26 24"><path d="M13 22S2 15 2 8a5.5 5.5 0 0 1 11-1 5.5 5.5 0 0 1 11 1c0 7-11 14-11 14z" fill="none" stroke="#fff" stroke-width="2.6"/></svg><svg width="16" height="14" viewBox="0 0 16 14"><path d="M1 13c1-6 5-8 10-8V1l5 5-5 5V8c-4 0-8 1-10 5z" fill="#fff"/></svg></span></div>
    <div class="class-row"><svg width="18" height="18" viewBox="0 0 18 18"><circle cx="9" cy="9" r="7.5" fill="none" stroke="#fff" stroke-width="2"/><path d="M9 5v4H6" stroke="#fff" stroke-width="1.8" fill="none"/></svg><span class="name">Lorem Ipsum is simply</span><span class="tools"><svg width="15" height="15" viewBox="0 0 15 15"><rect x="1" y="2.5" width="13" height="11.5" fill="none" stroke="#fff" stroke-width="1.3"/><path d="M1 6h13M4 1v3M11 1v3M4 8.5h7M4 11h7M6 6v8M9 6v8" stroke="#fff" stroke-width="1"/></svg><svg width="16" height="14" viewBox="0 0 26 24"><path d="M13 22S2 15 2 8a5.5 5.5 0 0 1 11-1 5.5 5.5 0 0 1 11 1c0 7-11 14-11 14z" fill="none" stroke="#fff" stroke-width="2.6"/></svg><svg width="16" height="14" viewBox="0 0 16 14"><path d="M1 13c1-6 5-8 10-8V1l5 5-5 5V8c-4 0-8 1-10 5z" fill="#fff"/></svg></span></div>
  </div>

  <!-- events -->
  <h2 class="abs section-h" style="left:609px;top:740px;width:351px;text-align:center">NEXT EVENTS</h2>
  <div class="abs events">
    <div class="event" style="top:9px">
      <div class="photo thumb" role="img" aria-label="Woman in a triangle yoga pose outdoors at sunrise" style="background:linear-gradient(180deg,#cfd8c8 0%,#e8e2c6 45%,#7d8c5a 75%,#4c5a38 100%)"></div>
      <div class="body"><div class="date">Feb 14, 2016</div><div class="name">YOGA 1</div><p>Suspendisse potenti. Phasellus ac velit<br>vulputate, malesuada dolor at malesuada</p></div>
    </div>
    <div class="event" style="top:102px">
      <div class="photo thumb" role="img" aria-label="Person meditating on a mountain ridge facing the valley" style="background:linear-gradient(180deg,#c8d4dc 0%,#e2e6e4 40%,#8d9c78 65%,#5d7a3a 100%)"></div>
      <div class="body"><div class="date">Feb 21, 2016</div><div class="name">YOGA 2</div><p>Suspendisse potenti. Phasellus ac velit<br>vulputate, malesuada dolor at malesuada</p></div>
    </div>
  </div>

  <!-- blog -->
  <h2 class="abs section-h" style="left:242px;top:992px">BLOG</h2>
  <div class="abs pager" style="left:898px;top:994px"><svg width="16" height="16" viewBox="0 0 16 16"><circle cx="8" cy="8" r="8" fill="#b8d3a0"/><path d="M11 8H5M7.5 5L4.5 8l3 3" stroke="#fff" stroke-width="1.8" fill="none"/></svg><svg width="16" height="16" viewBox="0 0 16 16"><circle cx="8" cy="8" r="8" fill="var(--green-text)"/><path d="M5 8h6M8.5 5l3 3-3 3" stroke="#fff" stroke-width="1.8" fill="none"/></svg></div>

  <div class="abs post-date" style="left:247px;top:1034px">Feb<br>21,<br>2016</div>
  <div class="abs post-rule" style="left:293px;top:1028px"></div>
  <div class="abs post-icons" style="left:249px;top:1099px">
    <svg width="18" height="16" viewBox="0 0 26 24"><path d="M13 22S2 15 2 8a5.5 5.5 0 0 1 11-1 5.5 5.5 0 0 1 11 1c0 7-11 14-11 14z" fill="none" stroke="var(--green-text)" stroke-width="2.4"/></svg>
    <svg width="18" height="16" viewBox="0 0 18 16"><ellipse cx="9" cy="7" rx="8" ry="6" fill="none" stroke="var(--green-text)" stroke-width="1.6"/><path d="M4 12l-2 3 5-2" fill="var(--green-text)"/><circle cx="5.5" cy="7" r="1.1" fill="var(--green-text)"/><circle cx="9" cy="7" r="1.1" fill="var(--green-text)"/><circle cx="12.5" cy="7" r="1.1" fill="var(--green-text)"/></svg>
    <svg width="18" height="16" viewBox="0 0 18 16"><rect x="1" y="2" width="8" height="5" rx="2.5" transform="rotate(40 5 4.5)" fill="none" stroke="var(--green-text)" stroke-width="1.8"/><rect x="8" y="9" width="8" height="5" rx="2.5" transform="rotate(40 12 11.5)" fill="none" stroke="var(--green-text)" stroke-width="1.8"/></svg>
  </div>
  <div class="photo post-img abs" style="left:309px;top:1028px;background:linear-gradient(180deg,#6f8db5 0%,#b9c7d8 45%,#3d536d 100%)" role="img" aria-label="Silhouette of a person in a yoga pose reflected on water under a cloudy sky"></div>
  <div class="abs post-by" style="left:445px;top:1026px">Writter <span>Owen Pellick</span></div>
  <svg class="abs" style="left:438px;top:1089px" width="14" height="16" viewBox="0 0 14 16"><path d="M1 1h8l4 4v10H1z" fill="none" stroke="var(--green-text)" stroke-width="1.4"/><rect x="3.5" y="8" width="4.5" height="4" fill="var(--green-text)"/><path d="M8 10l3-2v4z" fill="var(--green-text)"/></svg>
  <div class="abs post-title" style="left:309px;top:1109px">YOGA TECNIQUE</div>
  <p class="abs post-text" style="left:309px;top:1127px">Morbi ut sodales mi. Quisque vulputate elit massa, et congue lacus aliquam vel. Integer vitae blandit ligula, non ornare velit. Nulla luctus, nulla fermentum sodales lobortis, turpis nisl dictum lorem, eu consequat libero enim eu diam.</p>

  <div class="abs post-date" style="left:611px;top:1034px">Feb<br>22,<br>2016</div>
  <div class="abs post-rule" style="left:657px;top:1028px"></div>
  <div class="abs post-icons" style="left:613px;top:1099px">
    <svg width="18" height="16" viewBox="0 0 26 24"><path d="M13 22S2 15 2 8a5.5 5.5 0 0 1 11-1 5.5 5.5 0 0 1 11 1c0 7-11 14-11 14z" fill="none" stroke="var(--green-text)" stroke-width="2.4"/></svg>
    <svg width="18" height="16" viewBox="0 0 18 16"><ellipse cx="9" cy="7" rx="8" ry="6" fill="none" stroke="var(--green-text)" stroke-width="1.6"/><path d="M4 12l-2 3 5-2" fill="var(--green-text)"/><circle cx="5.5" cy="7" r="1.1" fill="var(--green-text)"/><circle cx="9" cy="7" r="1.1" fill="var(--green-text)"/><circle cx="12.5" cy="7" r="1.1" fill="var(--green-text)"/></svg>
    <svg width="18" height="16" viewBox="0 0 18 16"><rect x="1" y="2" width="8" height="5" rx="2.5" transform="rotate(40 5 4.5)" fill="none" stroke="var(--green-text)" stroke-width="1.8"/><rect x="8" y="9" width="8" height="5" rx="2.5" transform="rotate(40 12 11.5)" fill="none" stroke="var(--green-text)" stroke-width="1.8"/></svg>
  </div>
  <div class="photo post-img abs" style="left:672px;top:1026px;width:110px;height:80px;background:linear-gradient(180deg,#f2c27a 0%,#e8a150 40%,#8a5a32 100%)" role="img" aria-label="Group of people meditating on a beach at sunset"></div>
  <div class="abs post-by" style="left:800px;top:1027px">Writter <span>Owen Pellick</span></div>
  <svg class="abs" style="left:802px;top:1089px" width="14" height="16" viewBox="0 0 14 16"><path d="M1 1h8l4 4v10H1z" fill="none" stroke="var(--green-text)" stroke-width="1.4"/><rect x="3.5" y="8" width="4.5" height="4" fill="var(--green-text)"/><path d="M8 10l3-2v4z" fill="var(--green-text)"/></svg>
  <div class="abs post-title" style="left:672px;top:1109px">YOGA TECNIQUE 2</div>
  <p class="abs post-text" style="left:672px;top:1127px">Morbi ut sodales mi. Quisque vulputate elit massa, et congue lacus aliquam vel. Integer vitae blandit ligula, non ornare velit. Nulla luctus, nulla fermentum sodales lobortis, turpis nisl dictum lorem, eu consequat libero enim eu diam.</p>

  <!-- gallery -->
  <h2 class="abs section-h" style="left:241px;top:1235px">GALLERY</h2>
  <div class="abs pager" style="left:897px;top:1232px"><svg width="16" height="16" viewBox="0 0 16 16"><circle cx="8" cy="8" r="8" fill="#b8d3a0"/><path d="M11 8H5M7.5 5L4.5 8l3 3" stroke="#fff" stroke-width="1.8" fill="none"/></svg><svg width="16" height="16" viewBox="0 0 16 16"><circle cx="8" cy="8" r="8" fill="var(--green-text)"/><path d="M5 8h6M8.5 5l3 3-3 3" stroke="#fff" stroke-width="1.8" fill="none"/></svg></div>
  <div class="photo gallery-item" style="left:240px;background:linear-gradient(180deg,#c7d6a8 0%,#e6e0cf 50%,#7ea24e 100%)" role="img" aria-label="Man meditating cross-legged on grass"></div>
  <div class="photo gallery-item" style="left:387px;background:linear-gradient(180deg,#f5a742 0%,#f8d36a 45%,#d7692a 100%)" role="img" aria-label="Silhouette in a standing yoga pose on a rock at sunset"></div>
  <div class="photo gallery-item" style="left:534px;background:linear-gradient(180deg,#8a5a3a 0%,#b8c98a 50%,#6f8f4a 100%)" role="img" aria-label="Older woman meditating in a garden"></div>
  <div class="photo gallery-item" style="left:680px;background:linear-gradient(180deg,#6c5a52 0%,#d9924a 55%,#3d2e2a 100%)" role="img" aria-label="Silhouette in a dancer yoga pose on a beach at dusk"></div>
  <div class="photo gallery-item" style="left:827px;background:linear-gradient(180deg,#f2d27a 0%,#f0b65a 50%,#5a8a9a 100%)" role="img" aria-label="Person meditating in shallow sea water at sunset"></div>

  <!-- footer -->
  <div class="abs copyright">OwenPellick.com All Rights Reserved Copyright 2013-2015</div>
  <div class="abs social" style="left:814px;background:#3b5998" role="img" aria-label="Social link"></div>
  <div class="abs social" style="left:855px;background:#3aaadf" role="img" aria-label="Social link"></div>
  <div class="abs social" style="left:896px;background:#dd4b39" role="img" aria-label="Social link"></div>
  <div class="abs social" style="left:937px;background:#0e76a8" role="img" aria-label="Social link"></div>
</div>
</body>
</html>
```